Harbourline Gas and Plumbing Business Card Design

I am after a business card design for my plumbing business called 'Harbourline Gas & Plumbing'. I do all types of plumbing and gas work and specialise in general maintenance plumbing. Would like to see designs using current logo

Industry/Entity Type

Plumbing

Contact Information for Business Card

Name - Dallas McTavish
Phone number - 0468305917
Email - admin@harbourlinegasandplumbing.com.au
ABN - 58104629375

```html
<!DOCTYPE html>
<html lang="en">
<head>
<meta charset="utf-8">
<title>Harbourline Gas &amp; Plumbing – Business Card</title>
<link rel="stylesheet" href="https://fonts.googleapis.com/css2?family=Russo+One&family=Open+Sans:wght@400;600&display=swap">
<style>
  :root {
    --stage: #2b2b2d;
    --blue-deep: #2a2fb8;
    --blue-mid: #1f4fd6;
    --blue-light: #2f7be8;
    --white: #ffffff;
    --name-gold: #f7c21b;
    --accent-orange: #f28a1e;
    --contact-text: #e9eefc;
  }
  * { box-sizing: border-box; margin: 0; padding: 0; }
  html, body {
    width: 1200px; height: 960px; overflow: hidden;
    background: var(--stage);
  }
  .canvas {
    width: 1200px; height: 960px;
    display: flex; flex-direction: column; align-items: center; justify-content: center;
    gap: 30px;
  }
  .card {
    width: 760px; height: 434px;
    position: relative; overflow: hidden;
    box-shadow: 0 10px 28px rgba(0,0,0,.45);
  }
  .card--front {
    background: radial-gradient(ellipse at 50% 95%, var(--blue-light) 0%, var(--blue-mid) 40%, var(--blue-deep) 100%);
  }
  .card--back {
    background: radial-gradient(ellipse at 70% 100%, var(--blue-light) 0%, var(--blue-mid) 45%, var(--blue-deep) 100%);
  }
  .brand {
    position: absolute;
    font-family: "Russo One", sans-serif;
    color: var(--white);
    text-transform: uppercase;
    line-height: 1.05;
    display: flex; align-items: center; gap: 18px;
  }
  .brand__dot {
    width: 58px; height: 58px; border-radius: 50%;
    background: var(--white); flex: none;
  }
  .brand__name { display: block; }
  .card--front .brand { left: 150px; top: 160px; font-size: 46px; letter-spacing: 1px; }
  .card--front .brand small { font-size: 25px; letter-spacing: 2px; }
  .card--back .brand { left: 330px; top: 58px; font-size: 40px; letter-spacing: 1px; }
  .card--back .brand small { font-size: 21px; letter-spacing: 2px; }
  .brand-panel {
    position: absolute; left: 0; top: 0; width: 300px; height: 434px;
  }
  .contact {
    position: absolute; left: 360px; top: 232px;
    font-family: "Open Sans", sans-serif; color: var(--contact-text);
  }
  .contact__name {
    font-family: "Open Sans", sans-serif; font-weight: 600;
    font-size: 26px; color: var(--name-gold); text-transform: uppercase;
    margin-bottom: 14px;
  }
  .contact__line {
    display: flex; align-items: center; gap: 10px;
    font-size: 17px; line-height: 30px;
  }
  .contact__line svg { width: 16px; height: 16px; flex: none; }
  .contact__line--plain { padding-left: 0; }
</style>
</head>
<body>
<main class="canvas">
  <section class="card card--front" aria-label="Card front">
    <div class="brand">
      <span class="brand__dot"></span>
      <span class="brand__name">Harbourline<br><small>Gas &amp; Plumbing</small></span>
    </div>
  </section>

  <section class="card card--back" aria-label="Card back">
    <svg class="brand-panel" viewBox="0 0 300 434" aria-hidden="true">
      <path d="M0 0 H205 C250 60 215 120 250 190 C285 260 240 350 255 434 H0 Z" fill="var(--white)"/>
      <path d="M205 0 C250 60 215 120 250 190 C285 260 240 350 255 434" fill="none" stroke="var(--accent-orange)" stroke-width="5"/>
    </svg>
    <div class="brand">
      <span class="brand__name">Harbourline<br><small>Gas &amp; Plumbing</small></span>
    </div>
    <div class="contact">
      <p class="contact__name">Dallas McTavish</p>
      <p class="contact__line">
        <svg viewBox="0 0 24 24" aria-hidden="true"><path fill="var(--accent-orange)" d="M6.6 10.8a15.1 15.1 0 0 0 6.6 6.6l2.2-2.2a1 1 0 0 1 1-.25 11.4 11.4 0 0 0 3.6.57 1 1 0 0 1 1 1V20a1 1 0 0 1-1 1A17 17 0 0 1 3 4a1 1 0 0 1 1-1h3.5a1 1 0 0 1 1 1c0 1.25.2 2.45.57 3.57a1 1 0 0 1-.25 1z"/></svg>
        0468305917
      </p>
      <p class="contact__line">
        <svg viewBox="0 0 24 24" aria-hidden="true"><rect x="2" y="5" width="20" height="14" rx="2" fill="var(--accent-orange)"/><path d="M3 6l9 7 9-7" fill="none" stroke="var(--white)" stroke-width="1.8"/></svg>
        admin@harbourlinegasandplumbing.com.au
      </p>
      <p class="contact__line contact__line--plain">ABN 58104629375</p>
    </div>
  </section>
</main>
</body>
</html>
```